Mac IT Support company needs a flyer

This flyer will be delivered by hand to prospective customers in a door drop campaign.
Double sided A6
We support SMEs in Central London mainly Mac networks. We also supply managed services including email and internet connectivity.
The target audience is office managers, receptionists and business owners.
It will be extremely simple and illustration mainly.
Any ideas are welcome but we quite like the following:
A text poster saying
"Make IT easy" or something like that.
An illustration of two people, the client and us. Us juggling web, IT etc and the Client able to concentrate on their job.
Copy is being written by a professional copywriter, content of which will depend on the flyer design.
Target Market(s)
Small SMEs using Orchard Mac computers, design companies, agencies etc.
Industry/Entity Type
Technical Service
Requirements
Must have
- Our number - 0207 946 0581
- Our email - info@brightloop.example
- Our web address - www.brightloop.example
Nice to have
- Some clever eye catching designs
Should not have
- Too much text
- Overly complicated design

```html
<!DOCTYPE html>
<html lang="en">
<head>
<meta charset="utf-8">
<title>Brightloop – IT Support Flyer</title>
<link rel="stylesheet" href="https://fonts.googleapis.com/css2?family=Jost:wght@300;400;500;600;700&display=swap">
<style>
  :root {
    --backdrop: #2e2e2e;
    --paper: #ffffff;
    --lime: #a8cb3c;
    --lime-bright: #c1d92e;
    --ink: #1c1c1c;
    --footer-grey: #6a6a6a;
    --screen-dark: #2f2f2f;
    --photo-light: #c9d3dc;
    --photo-dark: #5d6a78;
  }
  * { margin: 0; padding: 0; box-sizing: border-box; }
  html, body { width: 1200px; height: 942px; overflow: hidden; }
  body {
    background: var(--backdrop);
    font-family: "Jost", "Century Gothic", sans-serif;
    color: var(--ink);
    position: relative;
  }
  .flyer {
    position: absolute;
    width: 496px;
    height: 712px;
    background: var(--paper);
    overflow: hidden;
  }
  .flyer--front { left: 43px; top: 36px; }
  .flyer--back { left: 632px; top: 150px; }

  .notch {
    position: absolute;
    width: 0; height: 0;
    border-left: 9px solid transparent;
    border-right: 9px solid transparent;
    border-top: 16px solid var(--paper);
    z-index: 3;
  }

  /* Front */
  .brand-mark {
    position: absolute;
    font-weight: 600;
    letter-spacing: 0.5px;
  }
  .flyer--front .brand-mark {
    left: 0; right: 0; top: 42px;
    text-align: center;
    font-size: 56px;
    color: var(--lime);
  }
  .hero {
    position: absolute;
    left: 0; top: 142px;
    width: 100%; height: 280px;
    background: var(--lime);
  }
  .hero-strip {
    position: absolute;
    left: 0; top: 422px;
    width: 100%; height: 40px;
    background: var(--lime-bright);
  }
  .hero-title {
    position: absolute;
    left: 36px; top: 204px;
    color: var(--paper);
    font-weight: 400;
    font-size: 65px;
    line-height: 76px;
    letter-spacing: 0.5px;
    z-index: 2;
  }
  .monitor-screen {
    position: absolute;
    left: 280px; top: 172px;
    width: 230px; height: 220px;
    background: linear-gradient(180deg, #3a3a3a, var(--screen-dark));
    border-radius: 8px;
    z-index: 2;
  }
  .monitor-screen span {
    position: absolute;
    left: 58px; top: 50px;
    color: var(--paper);
    font-weight: 600;
    font-size: 29px;
    line-height: 40px;
    letter-spacing: 1px;
  }
  .monitor-stand {
    position: absolute;
    left: 410px; top: 392px;
    width: 90px; height: 56px;
    background: linear-gradient(180deg, #d9d9d9, #a9a9a9);
    border-radius: 0 0 4px 4px;
    z-index: 1;
  }
  .intro {
    position: absolute;
    left: 38px; top: 516px;
    width: 420px;
    font-size: 16.5px;
    line-height: 23.5px;
    text-align: justify;
    hyphens: auto;
  }
  .intro .name { color: var(--lime); font-weight: 500; }
  .intro strong { font-weight: 600; }
  .footer {
    position: absolute;
    left: 0; bottom: 0;
    width: 100%;
    background: var(--footer-grey);
    color: var(--paper);
  }
  .flyer--front .footer { height: 53px; }
  .footer-url {
    position: absolute;
    right: 34px; top: 14px;
    font-size: 17px;
    font-weight: 600;
    letter-spacing: 0.5px;
  }

  /* Back */
  .photo {
    position: absolute;
    left: 0; top: 0;
    width: 100%; height: 272px;
    background: linear-gradient(135deg, var(--photo-light) 0%, #aab6c2 45%, var(--photo-dark) 100%);
  }
  .back-band {
    position: absolute;
    left: 0; top: 272px;
    width: 100%; height: 40px;
    background: var(--lime-bright);
  }
  .back-band-notch {
    position: absolute;
    left: 228px; top: 312px;
    width: 0; height: 0;
    border-left: 9px solid transparent;
    border-right: 9px solid transparent;
    border-top: 16px solid var(--lime-bright);
  }
  .services-title {
    position: absolute;
    left: 26px; top: 348px;
    font-size: 23px;
    font-weight: 400;
  }
  .services {
    position: absolute;
    list-style: none;
    font-size: 17px;
    line-height: 23.5px;
  }
  .services--left { left: 22px; top: 390px; }
  .services--right { left: 262px; top: 410px; }
  .services li::before {
    content: "\2713";
    color: var(--lime);
    font-weight: 700;
    margin-right: 5px;
  }
  .flyer--back .footer { height: 164px; }
  .flyer--back .brand-mark {
    left: 24px; top: 60px;
    font-size: 34px;
    color: var(--paper);
  }
  .contact {
    position: absolute;
    left: 250px; right: 18px; top: 22px;
    font-size: 15px;
    line-height: 25px;
    list-style: none;
    letter-spacing: 0.3px;
    white-space: nowrap;
  }
  .contact-heading {
    font-weight: 600;
    font-size: 18px;
    margin-bottom: 3px;
  }
  .contact li { display: flex; align-items: center; gap: 10px; }
  .contact svg { width: 16px; height: 16px; flex: none; }
</style>
</head>
<body>

<section class="flyer flyer--front" aria-label="Flyer front">
  <div class="brand-mark">Brightloop</div>
  <span class="notch" style="left:239px; top:142px;"></span>
  <div class="hero"></div>
  <div class="hero-strip"></div>
  <span class="notch" style="left:239px; top:462px; border-top-color: var(--lime-bright);"></span>
  <h1 class="hero-title">MAKE<br>IT EASY</h1>
  <div class="monitor-stand"></div>
  <div class="monitor-screen"><span>YOUR<br>DESIGN<br>HERE</span></div>
  <p class="intro"><span class="name">Brightloop</span> was formed in 2004 as an IT support company servicing London's advertising and media companies. In the last 11 years we've grown to support all three major platforms: <strong>Orchard, Paneware and Penguix.</strong></p>
  <footer class="footer">
    <span class="notch" style="left:239px; top:0;"></span>
    <span class="footer-url">www.brightloop.example</span>
  </footer>
</section>

<section class="flyer flyer--back" aria-label="Flyer back">
  <div class="photo" role="img" aria-label="Photo of two colleagues working at computers in a bright office"></div>
  <div class="back-band"></div>
  <span class="back-band-notch"></span>
  <h2 class="services-title">Our Services</h2>
  <ul class="services services--left">
    <li>IT Support</li>
    <li>IT Consultancy</li>
    <li>IT Project Management</li>
    <li>Cloud Based Backup</li>
    <li>Internet Connectivity</li>
  </ul>
  <ul class="services services--right">
    <li>Cloud Based Email</li>
    <li>Relocation</li>
    <li>Monitoring</li>
    <li>Spam Prevation</li>
  </ul>
  <footer class="footer">
    <span class="notch" style="left:228px; top:0;"></span>
    <div class="brand-mark">Brightloop</div>
    <ul class="contact">
      <li class="contact-heading">Contact us now!</li>
      <li>
        <svg viewBox="0 0 24 24" aria-hidden="true"><path fill="#fff" d="M6.6 10.8a15.1 15.1 0 0 0 6.6 6.6l2.2-2.2c.3-.3.7-.4 1-.2 1.1.4 2.3.6 3.6.6.6 0 1 .4 1 1V20c0 .6-.4 1-1 1A17 17 0 0 1 3 4c0-.6.4-1 1-1h3.5c.6 0 1 .4 1 1 0 1.3.2 2.5.6 3.6.1.3 0 .7-.2 1z"/></svg>
        0207 946 0581
      </li>
      <li>
        <svg viewBox="0 0 24 24" aria-hidden="true"><rect x="2" y="5" width="20" height="14" fill="#fff"/><path d="M2 5l10 8 10-8" fill="none" stroke="#6a6a6a" stroke-width="1.8"/></svg>
        info@brightloop.example
      </li>
      <li>
        <svg viewBox="0 0 24 24" aria-hidden="true"><circle cx="12" cy="12" r="10" fill="#fff"/><path d="M2 12h20M12 2c3 3 3 17 0 20M12 2c-3 3-3 17 0 20" fill="none" stroke="#6a6a6a" stroke-width="1.5"/></svg>
        www.brightloop.example
      </li>
    </ul>
  </footer>
</section>

</body>
</html>
```